Award-winnning Estate Agent needs a premium version of their 'For Sale' board design

We need a premium option for our 'For Sale' board design. We have a standard board that is attached to this brief, but were are looking to have a premium design version that we will use when selling exclusive properties. Our company name is Harbour Lane Estates and the name for this is exclusive selection is: 'The Harbour Collection'. The design needs to work with our current brand, but have a distinctive PREMIUM feel to it. I have uploaded the barnd guidelines and also some of the exisisting logo variations. We do NOT need a new logo but feel free to play around with colours, fonts, sizes etc. for the sign.

Target Market(s)

Property buyers & house hunters

Industry/Entity Type

Real Estate - Residential Property

Font styles to use
Sans Serif

Requirements
Must have
• A premium fee, must be square design, must be easy to read when driving past the sign
Nice to have
• I'm open ot ideas

```html
<!DOCTYPE html>
<html lang="en">
<head>
<meta charset="utf-8">
<title>Harbour Lane Estates – For Sale Board</title>
<link rel="stylesheet" href="https://fonts.googleapis.com/css2?family=Anton&family=Arimo:wght@700&display=swap">
<style>
  :root {
    --sky-light: #8fe6fd;
    --sky-mid: #62e0ff;
    --sky-deep: #33d8ff;
    --brand-cyan: #4dd8fc;
    --brand-navy: #000ef0;
    --brand-blue: #2980ff;
    --board-white: #ffffff;
  }
  html, body {
    margin: 0;
    padding: 0;
    width: 1200px;
    height: 1200px;
    overflow: hidden;
    background: var(--sky-mid);
  }
  .sale-board {
    display: block;
    width: 1200px;
    height: 1200px;
  }
  .board-panel { fill: var(--board-white); }
  .board-frame { fill: none; stroke: var(--brand-cyan); stroke-width: 4; }
  .brand-mark { fill: var(--brand-blue); }
  .brand-name {
    font-family: "Arimo", Arial, sans-serif;
    font-weight: 700;
    fill: var(--brand-navy);
  }
  .collection-title,
  .sale-headline,
  .web-address {
    font-family: "Anton", "Arial Narrow", sans-serif;
    fill: var(--brand-cyan);
  }
  .phone-band { fill: var(--brand-cyan); }
  .phone-number {
    font-family: "Anton", "Arial Narrow", sans-serif;
    fill: var(--board-white);
  }
</style>
</head>
<body>
<svg class="sale-board" viewBox="0 0 1200 1200" xmlns="http://www.w3.org/2000/svg">
  <defs>
    <linearGradient id="sky-wash" x1="0" y1="1" x2="1" y2="0">
      <stop offset="0" stop-color="var(--sky-deep)"/>
      <stop offset="0.5" stop-color="var(--sky-mid)"/>
      <stop offset="1" stop-color="var(--sky-light)"/>
    </linearGradient>
  </defs>

  <rect class="backdrop" x="0" y="0" width="1200" height="1200" fill="url(#sky-wash)"
        role="img" aria-label="Faceted light blue geometric backdrop"/>

  <rect class="board-panel" x="107" y="104" width="987" height="987"/>
  <rect class="board-frame" x="134" y="131" width="933" height="933"/>

  <rect class="brand-mark" x="520" y="200" width="160" height="160"/>

  <text class="brand-name" x="600" y="523" font-size="72" text-anchor="middle"
        textLength="716" lengthAdjust="spacingAndGlyphs">Harbour Lane Estates</text>

  <text class="collection-title" x="202" y="619" font-size="64"
        textLength="798" lengthAdjust="spacingAndGlyphs">THE HARBOUR COLLECTION</text>

  <text class="sale-headline" x="204" y="802" font-size="208"
        textLength="796" lengthAdjust="spacingAndGlyphs">FOR SALE</text>

  <rect class="phone-band" x="204" y="832" width="796" height="129"/>
  <text class="phone-number" x="250" y="938" font-size="111"
        textLength="701" lengthAdjust="spacingAndGlyphs">01632 960714</text>

  <text class="web-address" x="204" y="1045" font-size="45"
        textLength="797" lengthAdjust="spacingAndGlyphs">WWW.HARBOURLANEESTATES.CO.UK</text>
</svg>
</body>
</html>
```